Mail order Nursery needs banner for promoting perennials that compliment roses.

banner should be 1135 wide x165 tall. We have an existing one displayed but we are not happy with the way it is washed out. Use your creativity to give us something that pops. Would love to see some watercolor or some other form of image other than just words washed across a stock photo. Banner needs to read Perennial Companions for Roses or some variation of that. Colors need to compliment our current theme. You can view the page and banner I want to replace at www.themeadowbellplot.com. The banner we want to replace has been uploaded to the pixel harbor file drop box. Thanks for your help and I look forward to seeing what you guys come up with. EDIT: I don't think I was clear enough in by brief. This banner promotes the sale of plants that look good planted with roses. We are getting to many submissions that are using only roses as the backdrop. We are looking for different types of plants that you would grow in your garden to compliment your roses. Thanks for all your hard work.

Target Market(s)

Home owners between 30 and 65

Industry/Entity Type

Nursery

Colors
33a6d7
e667a6

Requirements
Must have
• Text promotion perennials that compliment roses.... does not have to be those exact words but get the point across
Should not have
• Stock Photos with simple text washed across it.

```html
<!DOCTYPE html>
<html lang="en">
<head>
<meta charset="utf-8">
<title>Perennial Companions for Roses – Banner</title>
<link href="https://fonts.googleapis.com/css2?family=Berkshire+Swash&family=Lobster+Two:ital,wght@1,700&display=swap" rel="stylesheet">
<style>
  :root {
    --wood-dark: #3a3733;
    --wood-mid: #524d47;
    --wood-light: #665f56;
    --plank-gap: rgba(20, 18, 16, 0.55);
    --frame-blue: #33a6d7;
    --band-mauve: #7b4d60;
    --title-white: #ffffff;
    --tagline-blue: #2a9ed8;
    --bloom-pink: #e98aa8;
    --bloom-peach: #f2b27e;
    --bloom-red: #d8434f;
    --leaf-green: #4f9a82;
    --lavender: #9c88c8;
    --butterfly-orange: #f08a5a;
  }
  html, body {
    margin: 0;
    padding: 0;
    width: 1200px;
    height: 174px;
    overflow: hidden;
    background: var(--wood-dark);
  }
  .banner {
    position: relative;
    width: 1200px;
    height: 174px;
    overflow: hidden;
  }
  .wood-backdrop {
    position: absolute;
    inset: 0;
    background:
      repeating-linear-gradient(180deg, transparent 0 31px, var(--plank-gap) 31px 33px),
      repeating-linear-gradient(90deg, rgba(255,255,255,0.03) 0 3px, transparent 3px 9px),
      linear-gradient(90deg, var(--wood-dark), var(--wood-mid) 30%, var(--wood-light) 55%, var(--wood-mid) 80%, var(--wood-dark));
  }

  /* flower artwork zones */
  .art { position: absolute; }
  .art-vine-top {
    left: 40px; top: 0; width: 470px; height: 26px;
    background: linear-gradient(90deg, rgba(79,154,130,0.75), rgba(156,136,200,0.7) 30%, rgba(79,154,130,0.55) 60%, rgba(79,154,130,0));
    border-radius: 0 0 40px 40px;
  }
  .art-garden-left {
    left: 0; top: 40px; width: 160px; height: 134px;
    background: linear-gradient(160deg, rgba(156,136,200,0.85) 0%, rgba(79,154,130,0.8) 35%, var(--bloom-pink) 60%, var(--bloom-peach) 100%);
    border-radius: 0 70px 0 0;
  }
  .art-foliage-bottom {
    left: 140px; top: 150px; width: 180px; height: 24px;
    background: linear-gradient(90deg, rgba(79,154,130,0.8), rgba(79,154,130,0));
    border-radius: 30px 30px 0 0;
  }
  .art-butterfly {
    left: 862px; top: 38px; width: 30px; height: 32px;
    background: var(--butterfly-orange);
    border-radius: 30% 60% 40% 50%;
  }
  .art-garden-right {
    left: 930px; top: 0; width: 270px; height: 174px;
    background: linear-gradient(200deg, var(--bloom-red) 0%, var(--bloom-pink) 28%, var(--bloom-peach) 40%, rgba(79,154,130,0.85) 62%, var(--lavender) 100%);
    border-radius: 90px 0 0 0;
  }

  /* title block */
  .title-frame {
    position: absolute;
    left: 137px;
    top: 42px;
    width: 732px;
    height: 72px;
    border: 3px solid var(--frame-blue);
    box-sizing: border-box;
  }
  .title-band {
    position: absolute;
    left: 155px;
    top: 23px;
    width: 697px;
    height: 80px;
    background: var(--band-mauve);
    opacity: 0.93;
    display: flex;
    align-items: center;
    padding-left: 56px;
    box-sizing: border-box;
  }
  .title {
    margin: 0;
    font-family: "Berkshire Swash", cursive;
    font-weight: 400;
    font-size: 41px;
    line-height: 1;
    color: var(--title-white);
    white-space: nowrap;
  }
  .tagline {
    position: absolute;
    left: 355px;
    top: 120px;
    margin: 0;
    font-family: "Lobster Two", cursive;
    font-style: italic;
    font-weight: 700;
    font-size: 34px;
    line-height: 1;
    letter-spacing: 0.6px;
    color: var(--tagline-blue);
    white-space: nowrap;
  }
</style>
</head>
<body>
  <div class="banner">
    <div class="wood-backdrop" role="img" aria-label="Weathered grey-brown wooden plank background"></div>

    <div class="art art-vine-top" role="img" aria-label="Watercolor sweet pea blooms and ivy trailing along the top edge"></div>
    <div class="art art-garden-left" role="img" aria-label="Watercolor lavender spikes, leaves and pink and peach garden roses"></div>
    <div class="art art-foliage-bottom" role="img" aria-label="Watercolor green leaves along the bottom edge"></div>

    <div class="title-frame"></div>
    <div class="title-band">
      <h1 class="title">Perennial Companions for Roses</h1>
    </div>
    <p class="tagline">Make Your Roses Even More Beautiful</p>

    <div class="art art-butterfly" role="img" aria-label="Small watercolor orange butterfly"></div>
    <div class="art art-garden-right" role="img" aria-label="Watercolor red, pink and peach roses with foxglove buds, foliage and lavender"></div>
  </div>
</body>
</html>
```